Home Health Agency Marketing Portfolio Booklet

We need a 4 page plus cover (total of 8 pages including front and back cover) design of a Home health Agency Marketing Booklet.
We specialize in taking care of homebound senior patients who needs specialize nursing and medical services in the comfort of their homes. We would like to see a design showing the caring and compassionate nature of our agency. The design should show a nice clean modern layout with nice font selection. Attached is a copy of our logo that needs to be use in the brochure. The colors of the logo should be use in the design of the brochure.
The design will consist of the Front and back cover, inside pages of the cover will be blank but there will be folded pockets that will need some design/color. The inside 4 pages will be full cover, double sided and will have all the information of the company.
The Marketing booklet will be 9"x 12".

```html
<!DOCTYPE html>
<html lang="en">
<head>
<meta charset="utf-8">
<title>Brightway Home Care – Marketing Booklet</title>
<link href="https://fonts.googleapis.com/css2?family=Montserrat:wght@400;500;600;700;800&display=swap" rel="stylesheet">
<style>
  :root{
    --orange:#f39a2b;
    --blue:#1f9ad6;
    --ink:#3b3b3b;
    --muted:#6a6a6a;
    --paper:#ffffff;
    --backdrop:#dcdcde;
    --photo-warm:#cfc5b9;
    --photo-cool:#8ea6b8;
  }
  *{box-sizing:border-box;margin:0;padding:0}
  html,body{width:960px;height:1200px;overflow:hidden;background:var(--backdrop)}
  body{font-family:"Montserrat",sans-serif}
  .canvas{width:960px;height:1200px;display:flex;flex-direction:column;align-items:center;justify-content:center;gap:0}
  .defs{position:absolute;width:0;height:0;overflow:hidden}
  .spread{display:block;background:var(--paper);box-shadow:0 4px 14px rgba(0,0,0,.18)}
  .cover-spread{width:820px;height:547px}
  .pocket{width:820px;height:138px;overflow:visible;display:block}
  .inside-row{display:flex;gap:10px;margin-top:18px}
  .inside-spread{width:470px;height:313px}
  svg text{font-family:"Montserrat",sans-serif}
  .body-white{fill:var(--paper)}
  .body-ink{fill:var(--muted)}
  .heading-white{fill:var(--paper);font-weight:600}
  .heading-ink{fill:var(--ink);font-weight:600}
  .heading-orange{fill:var(--orange);font-weight:600}
  .pill-label{fill:var(--paper);font-weight:600;font-size:5px}
  .brand-name{fill:var(--blue);font-weight:700}
</style>
</head>
<body>
<main class="canvas">

  <!-- shared gradients and text blocks -->
  <svg class="defs" aria-hidden="true">
    <defs>
      <linearGradient id="photo-room" x1="0" y1="0" x2="1" y2="1">
        <stop offset="0" stop-color="#d8d0c6"/>
        <stop offset=".55" stop-color="#b9b3ab"/>
        <stop offset="1" stop-color="#7fa2bb"/>
      </linearGradient>
      <linearGradient id="photo-soft" x1="0" y1="0" x2="1" y2="1">
        <stop offset="0" stop-color="#e3ddd6"/>
        <stop offset="1" stop-color="#9fb3c2"/>
      </linearGradient>
      <linearGradient id="photo-kit" x1="0" y1="0" x2="1" y2="1">
        <stop offset="0" stop-color="#ffffff"/>
        <stop offset="1" stop-color="#e4e6e8"/>
      </linearGradient>
      <linearGradient id="tint-orange" x1="0" y1="0" x2="1" y2="0">
        <stop offset="0" stop-color="#f39a2b"/>
        <stop offset=".7" stop-color="#f2a444"/>
        <stop offset="1" stop-color="#f0ad5a"/>
      </linearGradient>

      <g id="para-wide" font-size="4">
        <text><tspan x="0" y="0">Lorem ipsum dolor sit amet, consectetuer adipiscing elit, sed diam nonummy nibh euismod tincidunt ut laoreet</tspan><tspan x="0" y="5.6">dolore magna aliquam erat volutpat. Ut wisi enim ad minim veniam, quis nostrud exerci tation ullamcorper</tspan><tspan x="0" y="11.2">suscipit lobortis nisl ut aliquip ex ea commodo consequat. Duis autem vel eum iriure dolor in hendrerit in</tspan><tspan x="0" y="16.8">vulputate velit esse molestie consequat, vel illum dolore eu feugiat nulla facilisis at vero eros et accumsan</tspan><tspan x="0" y="22.4">et iusto odio dignissim qui blandit praesent luptatum zzril delenit augue duis dolore te feugait nulla.</tspan></text>
      </g>
      <g id="para-narrow" font-size="3.6">
        <text><tspan x="0" y="0">Lorem ipsum dolor sit amet, consectetuer adipiscing elit,</tspan><tspan x="0" y="5">sed diam nonummy nibh euismod tincidunt ut laoreet dolore</tspan><tspan x="0" y="10">magna aliquam erat volutpat. Ut wisi enim ad minim veniam,</tspan><tspan x="0" y="15">quis nostrud exerci tation ullamcorper suscipit lobortis nisl</tspan><tspan x="0" y="20">ut aliquip ex ea commodo consequat. Duis autem vel eum</tspan><tspan x="0" y="25">iriure dolor in hendrerit in vulputate velit esse molestie</tspan><tspan x="0" y="30">consequat, vel illum dolore eu feugiat nulla facilisis.</tspan></text>
      </g>
      <g id="bullet-list" font-size="3.6">
        <text><tspan x="0" y="0">• Lorem ipsum dolor sit amet, consectetuer</tspan><tspan x="0" y="6">• Lorem ipsum dolor sit amet</tspan><tspan x="0" y="12">• Lorem ipsum dolor sit amet, adipiscing elit</tspan><tspan x="0" y="18">• Lorem ipsum dolor sit, consectetuer elit</tspan><tspan x="0" y="24">• Lorem ipsum dolor sit amet</tspan></text>
      </g>
    </defs>
  </svg>

  <!-- Outside cover: back page (left) and front page (right) -->
  <svg class="spread cover-spread" viewBox="0 0 714 476" aria-label="Outside cover">
    <rect width="714" height="476" fill="var(--paper)"/>
    <path class="cover-blue-band" d="M0,122 C250,330 500,395 714,343 V476 H330 C220,400 100,280 0,150 Z" fill="var(--blue)"/>
    <path class="cover-orange-band" d="M0,108 C260,300 520,362 714,316 V346 C500,396 250,332 0,126 Z" fill="var(--orange)"/>
    <path class="cover-photo" role="img" aria-label="Photo: a nurse showing a tablet to a senior woman resting in a bed at home"
          d="M0,0 H530 C600,8 670,50 714,118 V316 C520,360 260,300 0,108 Z" fill="url(#photo-room)"/>

    <g class="front-brand">
      <circle cx="606" cy="32" r="8" fill="var(--orange)"/>
      <text class="brand-name" x="619" y="30" font-size="9">BRIGHTWAY</text>
      <text class="brand-name" x="619" y="40" font-size="9">HOME CARE</text>
    </g>

    <g class="front-tagline" text-anchor="middle" fill="var(--paper)">
      <text x="535" y="417" font-size="9.5" font-weight="600">YOUR HOME IS NOW A</text>
      <text x="535" y="443" font-size="22" font-weight="800" letter-spacing=".3">THERAPY CENTER</text>
      <text x="535" y="457" font-size="8.5" font-weight="700">WITH US BY YOUR SIDE.</text>
    </g>

    <g class="back-brand">
      <circle cx="86" cy="348" r="5.5" fill="var(--orange)"/>
      <text class="brand-name" x="95" y="346" font-size="6.5">BRIGHTWAY</text>
      <text class="brand-name" x="95" y="354" font-size="6.5">HOME CARE</text>
    </g>

    <g class="back-contact" text-anchor="middle">
      <text class="heading-orange" x="111" y="384" font-size="7.5" font-weight="500">FOR MORE INFORMATION</text>
      <circle cx="111" cy="394" r="3.2" fill="var(--orange)"/>
      <text x="111" y="404" font-size="3.4" fill="var(--ink)">12 Harbour Lane, Millbrook Road, Eastwick EW4 2QT</text>
      <circle cx="111" cy="411" r="3.2" fill="var(--orange)"/>
      <text x="111" y="421" font-size="3.4" fill="var(--ink)" font-weight="600">0000 000 000, 0000 000 000</text>
      <circle cx="111" cy="428" r="3.2" fill="var(--orange)"/>
      <text x="111" y="438" font-size="3.4" fill="var(--ink)">info@brightwayhomecare.com</text>
      <circle cx="111" cy="445" r="3.2" fill="var(--orange)"/>
      <text x="111" y="455" font-size="3.4" fill="var(--ink)">brightwayhomecare.com</text>
    </g>
  </svg>

  <!-- Folded pocket die-line -->
  <svg class="pocket" viewBox="0 0 714 120" aria-label="Inside pocket flap">
    <path d="M-17,0 H354 C350,40 349,80 346,108 C345,116 340,120 332,120 H-9 Q-17,120 -17,112 Z"
          fill="var(--paper)" stroke="#9a9a9a" stroke-width=".8"/>
    <line x1="0" y1="0" x2="0" y2="120" stroke="#c4c4c4" stroke-width=".6"/>
  </svg>

  <div class="inside-row">
    <!-- Inside spread one: purpose / about -->
    <svg class="spread inside-spread" viewBox="0 0 714 476" aria-label="Inside pages one and two">
      <rect width="714" height="476" fill="var(--paper)"/>
      <rect class="purpose-backdrop" role="img" aria-label="Photo of a care room with an IV stand, tinted orange"
            width="357" height="476" fill="url(#tint-orange)"/>

      <g class="purpose-section">
        <rect x="34" y="38" width="14" height="10" rx="1" fill="none" stroke="var(--paper)" stroke-width="1.2"/>
        <text class="heading-white" x="66" y="48" font-size="8.5">OUR PURPOSE</text>
        <use href="#para-wide" x="32" y="68" class="body-white"/>
        <use href="#bullet-list" x="32" y="128" class="body-white"/>
      </g>
      <g class="goals-section">
        <circle cx="41" cy="205" r="6.5" fill="var(--blue)"/>
        <text class="heading-white" x="66" y="213" font-size="8.5">OUR GOALS</text>
        <use href="#para-wide" x="32" y="233" class="body-white"/>
        <use href="#para-wide" x="32" y="292" class="body-white"/>
      </g>
      <g class="objectives-section">
        <path d="M35,352 l6,-12 l6,12 M38,346 h6" fill="none" stroke="var(--paper)" stroke-width="1.2"/>
        <text class="heading-white" x="66" y="352" font-size="8.5">OUR OBJECTIVES</text>
        <use href="#para-wide" x="32" y="370" class="body-white"/>
        <use href="#para-wide" x="32" y="430" class="body-white"/>
      </g>

      <path d="M357,206 C420,262 520,270 714,252 V268 C520,284 410,276 357,236 Z" fill="var(--orange)"/>
      <path class="about-photo" role="img" aria-label="Photo: a doctor talking with a senior man at home"
            d="M357,0 H575 V250 C480,256 410,240 357,206 Z" fill="url(#photo-soft)"/>

      <g class="about-section">
        <text class="heading-ink" x="605" y="53" font-size="8">ABOUT US</text>
        <use href="#para-narrow" x="578" y="72" class="body-ink"/>
        <use href="#para-narrow" x="578" y="127" class="body-ink"/>
        <use href="#para-narrow" x="578" y="175" class="body-ink"/>
      </g>

      <g class="offer-section">
        <text class="heading-ink" x="373" y="276" font-size="8.5">WHAT WE OFFER</text>
        <rect x="371" y="281" width="80" height="9" rx="4.5" fill="var(--orange)"/>
        <text class="pill-label" x="377" y="287.8">PEDIATRIC CARE</text>
        <use href="#bullet-list" x="377" y="302" class="body-ink"/>
        <rect role="img" aria-label="Photo: a nurse in a mask giving a senior woman an injection"
              x="572" y="280" width="142" height="96" fill="url(#photo-soft)"/>
        <rect x="571" y="381" width="64" height="9" rx="4.5" fill="var(--orange)"/>
        <text class="pill-label" x="577" y="387.8">ADULT CARE</text>
        <use href="#bullet-list" x="577" y="401" class="body-ink"/>
        <rect role="img" aria-label="Photo: a nurse visiting a young girl at home"
              x="357" y="382" width="154" height="94" fill="url(#photo-room)"/>
      </g>
    </svg>

    <!-- Inside spread two: missions / services -->
    <svg class="spread inside-spread" viewBox="0 0 714 476" aria-label="Inside pages three and four">
      <rect width="714" height="476" fill="var(--paper)"/>

      <path d="M0,174 C150,222 280,196 357,150 V252 C250,250 120,252 0,258 Z" fill="var(--orange)"/>
      <path d="M0,258 C120,252 250,250 357,252 V256 C250,254 120,256 0,262 Z" fill="var(--blue)"/>
      <path class="mission-photo" role="img" aria-label="Photo: a male nurse helping a senior woman in a wheelchair exercise her arm"
            d="M0,0 H357 V150 C280,196 150,222 0,174 Z" fill="url(#photo-room)"/>

      <g class="mission-section">
        <text class="heading-white" x="32" y="237" font-size="8.5">OUR MISSIONS &amp; VISION</text>
        <use href="#para-wide" x="32" y="276" class="body-ink"/>
        <use href="#para-wide" x="32" y="312" class="body-ink"/>
        <use href="#para-wide" x="32" y="344" class="body-ink"/>
        <text class="heading-orange" x="32" y="400" font-size="8.5">WHY ARE WE BRIGHTWAY?</text>
        <use href="#para-wide" x="32" y="418" class="body-ink"/>
      </g>
      <path d="M280,476 C320,462 345,448 357,432 C372,448 400,464 430,476 Z" fill="var(--blue)"/>

      <path d="M357,0 H714 V4 C620,58 480,78 357,80 Z" fill="var(--orange)"/>
      <path d="M357,80 C480,78 620,58 714,4 V12 C620,64 480,84 357,85 Z" fill="var(--blue)"/>
      <text class="heading-white" x="397" y="40" font-size="8.5">OUR HOME HEALTH CARE</text>
      <text class="heading-white" x="397" y="52" font-size="8.5">SERVICES INCLUDE:</text>

      <rect role="img" aria-label="Photo: a white first aid box with a red cross and medicine"
            x="500" y="302" width="214" height="174" fill="url(#photo-kit)"/>

      <g class="services-grid">
        <rect x="393" y="88" width="96" height="9" rx="4.5" fill="var(--blue)"/>
        <text class="pill-label" x="398" y="94.8">In-Home Support Services</text>
        <use href="#para-narrow" x="395" y="107" class="body-ink"/>
        <rect x="546" y="88" width="80" height="9" rx="4.5" fill="var(--blue)"/>
        <text class="pill-label" x="551" y="94.8">Private Duty Nursing</text>
        <use href="#para-narrow" x="548" y="107" class="body-ink"/>

        <rect x="393" y="204" width="80" height="9" rx="4.5" fill="var(--blue)"/>
        <text class="pill-label" x="398" y="210.8">Family Care Provider</text>
        <use href="#para-narrow" x="395" y="223" class="body-ink"/>
        <rect x="546" y="204" width="48" height="9" rx="4.5" fill="var(--blue)"/>
        <text class="pill-label" x="551" y="210.8">Senior Care</text>
        <use href="#para-narrow" x="548" y="223" class="body-ink"/>

        <rect x="393" y="318" width="80" height="9" rx="4.5" fill="var(--blue)"/>
        <text class="pill-label" x="398" y="324.8">Pediatric Home Care</text>
        <use href="#para-narrow" x="395" y="337" class="body-ink"/>
      </g>
    </svg>
  </div>

</main>
</body>
</html>
```